Investment Management Firm Power point template

Kestrel Holdings is a real estate investment firm focused on buying commercial office and residential property in the UK. We produce powerpoint presentations for our Board of Directors, Investment Committee and also to external investors.

We are looking for a powerpoint design template which we can use for future presentations which provide a professional look and feel.

Our current website: http://www.kestrelholdings-example.co.uk/

Target Market(s)

Institution Investors, Board of Directors, Professionals

Industry/Entity Type

Real Estate

Requirements
Must have
• Leverage off the current logo and colour scheme. However, does not have to purely rely on this colour scheme.
• - Title page
• - Content Page
• - Slide where graphs can be incorporated
• - Slide where photos can be incorporated
• - Slide of UK Map which can show where the property portfolio is currently located
• - Other slides incorporating smart art or other designs that can be used for future presentations
Nice to have
• An example of graphics that we would love to have in the powerpoint pack which we can easily edit has been attached

```html
<!DOCTYPE html>
<html lang="en">
<head>
<meta charset="utf-8">
<title>Kestrel Holdings – Photo Slide</title>
<link rel="stylesheet" href="https://fonts.googleapis.com/css2?family=Titillium+Web:wght@300;400;600;700&display=swap">
<style>
  :root {
    --brand-blue: #1d5688;
    --band-blue: #2b6c9b;
    --caption-blue: rgba(46, 104, 150, 0.88);
    --white: #ffffff;
    --frame-line: #9bb5cc;
  }
  * { margin: 0; padding: 0; box-sizing: border-box; }
  html, body {
    width: 1200px;
    height: 900px;
    overflow: hidden;
    background: var(--white);
  }
  .slide {
    position: relative;
    width: 1200px;
    height: 900px;
    background: var(--white);
    font-family: "Titillium Web", "Segoe UI", Arial, sans-serif;
  }
  .slide-title {
    position: absolute;
    left: 36px;
    top: 26px;
    font-size: 36px;
    font-weight: 700;
    color: var(--brand-blue);
    letter-spacing: 0.2px;
  }
  .title-rule {
    position: absolute;
    left: 0;
    top: 70px;
    width: 290px;
    height: 3px;
    background: var(--brand-blue);
  }
  .photo-card {
    position: absolute;
    top: 117px;
    height: 705px;
    overflow: hidden;
  }
  .photo-card--left { left: 0; width: 552px; }
  .photo-card--right { left: 567px; width: 633px; }
  .photo {
    position: absolute;
    inset: 0;
  }
  .photo--towers {
    background: linear-gradient(200deg, #d9d4e8 0%, #c7c6e0 35%, #8e9fd0 60%, #4f6cb8 85%, #3f5ca8 100%);
  }
  .photo--loft {
    background: linear-gradient(180deg, #a9a7a2 0%, #d3d1cb 25%, #eceae4 50%, #d7d2c6 75%, #b9ab91 100%);
  }
  .caption {
    position: absolute;
    left: 0;
    right: 0;
    bottom: 0;
    height: 131px;
    background: var(--caption-blue);
    color: var(--white);
    font-size: 19.5px;
    font-weight: 300;
    line-height: 1.55;
    text-align: center;
    display: flex;
    align-items: center;
    justify-content: center;
    padding: 0 24px;
  }
  .footer-band {
    position: absolute;
    left: 0;
    top: 843px;
    width: 915px;
    height: 57px;
    background: var(--band-blue);
  }
  .brand-box {
    position: absolute;
    left: 917px;
    top: 843px;
    width: 276px;
    height: 50px;
    border: 1px solid var(--frame-line);
    background: var(--white);
    display: flex;
    align-items: center;
    gap: 14px;
    padding-left: 18px;
  }
  .brand-square {
    width: 26px;
    height: 26px;
    background: var(--brand-blue);
  }
  .brand-name {
    font-size: 27px;
    font-weight: 600;
    color: var(--brand-blue);
    white-space: nowrap;
  }
</style>
</head>
<body>
  <main class="slide">
    <h1 class="slide-title">Slide Title Here</h1>
    <div class="title-rule"></div>

    <section class="photo-card photo-card--left">
      <div class="photo photo--towers" role="img" aria-label="Photo looking up at glass office towers against a pale sky"></div>
      <p class="caption">While a property’s fundamentals are important to us, we put equal focus on the people who use and enjoy our spaces. The experience of being in our buildings</p>
    </section>

    <section class="photo-card photo-card--right">
      <div class="photo photo--loft" role="img" aria-label="Photo of a bright loft apartment interior with tall windows, a plant and a modern kitchen"></div>
      <p class="caption">While a property’s fundamentals are important to us, we put equal focus on the people who use and enjoy our spaces. The experience of being in our buildings</p>
    </section>

    <div class="footer-band"></div>
    <div class="brand-box">
      <span class="brand-square"></span>
      <span class="brand-name">Kestrel Holdings</span>
    </div>
  </main>
</body>
</html>
```